Brochure Design Project

Please design a corporate brochure for my business "Corvin Asbestos & Safety"

Specs:-
- A4 flat size, three panel front, three panel back, roll-folded to DL
- Portrait orientation
- Full colour
Updates

Please don't forget to send in your designs. I believe the competition ends in a few hours. Thank you!

Target Market(s)

Business owners, commercial/industrial building owners, real estate property managers, strata managers

Industry/Entity Type

Business

Requirements
Must have
• - Professional / modern but serious as the content is important
- Cover page in particular must stand out so it will be noticeable if sitting on someone's desk
- Good use of whitespace and not too crowded
- Heading highlighted in warm/hot colour i.e. burnt orange, all other text in black
- Font Georgia 11pt
Nice to have
• - I have uploaded our letterhead source files too - please weave in the theme/look and feel of the letterhead into the brochure if possible.

```html
<!DOCTYPE html>
<html lang="en">
<head>
<meta charset="utf-8">
<title>Asbestos Brochure – Inside Spread</title>
<link rel="stylesheet" href="https://fonts.googleapis.com/css2?family=Gelasio:ital,wght@0,400;0,700;1,400&display=swap">
<style>
  :root {
    --backdrop: #e9e7e3;
    --paper: #e3e4e3;
    --heading: #e8822a;
    --ink: #141414;
    --tape: #f2e51c;
    --tape-deep: #e6d40e;
    --haze: #c9c6c6;
    --haze-warm: #a99594;
  }
  * { box-sizing: border-box; margin: 0; padding: 0; }
  html, body {
    width: 1200px; height: 840px; overflow: hidden;
    background: var(--backdrop);
  }
  .spread {
    position: absolute; left: 40px; top: 24px;
    width: 1120px; height: 792px;
    background: var(--paper);
    overflow: hidden;
    font-family: "Gelasio", Georgia, serif;
    color: var(--ink);
    box-shadow: 0 2px 10px rgba(0,0,0,0.12);
  }
  .hazard-photo {
    position: absolute; left: 0; top: 330px; width: 100%; height: 462px;
    background: linear-gradient(180deg, rgba(201,198,198,0) 0%, var(--haze) 22%, var(--haze-warm) 45%, var(--haze) 80%, #d6d7d8 100%);
  }
  .hazard-tape {
    position: absolute; left: 0; top: 435px; width: 880px; height: 216px;
    background: linear-gradient(90deg, var(--tape) 0%, var(--tape-deep) 75%, rgba(230,212,14,0) 100%);
  }
  .panel-fade {
    position: absolute; left: 760px; top: 0; width: 360px; height: 100%;
    background: linear-gradient(90deg, rgba(227,228,227,0) 0%, rgba(227,228,227,0.85) 18%, rgba(227,228,227,0.9) 100%);
  }
  .panel {
    position: absolute; top: 44px; width: 303px;
    font-size: 14px; line-height: 14.6px;
  }
  .panel--left { left: 36px; }
  .panel--middle { left: 409px; }
  .panel--right { left: 782px; width: 302px; }
  .panel h2 {
    color: var(--heading);
    font-size: 18px; line-height: 18.5px; font-weight: 700;
    margin-bottom: 16px;
  }
  .panel--right h2 { margin-bottom: 12px; }
  .panel p { text-align: justify; margin-bottom: 15px; }
  .panel em { font-style: italic; }
  .panel strong { font-weight: 700; }
  .panel sup { font-size: 7px; }
  .checklist { list-style: none; margin: 0 0 12px 0; }
  .checklist li {
    position: relative; padding-left: 48px; text-align: justify;
  }
  .checklist li::before {
    content: ""; position: absolute; left: 29px; top: 5px;
    width: 5px; height: 5px; background: var(--ink);
  }
  .list-intro { margin-bottom: 0 !important; text-align: left !important; }
</style>
</head>
<body>
  <div class="spread">
    <div class="hazard-photo" role="img" aria-label="Photograph of yellow asbestos danger warning tape across a hazy background"></div>
    <div class="hazard-tape" role="img" aria-label="Yellow danger asbestos warning tape"></div>
    <div class="panel-fade"></div>

    <section class="panel panel--left">
      <h2>Why is<br>Asbestos so dangerous?</h2>
      <p>Asbestos is a hazardous substance that poses a risk to health by inhalation if the asbestos fibres become airborne. Exposure to these fibres is known to cause mesothelioma, asbestosis and lung cancer.</p>
      <p>Australia had the highest per capita use of asbestos in the world in the 1950s and it is not surprising that it has the world's highest incidence of asbestos related cancer. Asbestos has caused a significant death toll and much suffering in Australia, and the impact of asbestos-related diseases is expected to peak in 2020.</p>
    </section>

    <section class="panel panel--middle">
      <h2>Are you compliant with current Work Health and Safety (WHS)Legislation regarding Asbestos?</h2>
      <p>The Work Health and Safety (WHS) Regulation (2011) and its associated <em>Code of Practice – How to Manage and Control Asbestos in the Workplace</em> requires that all non-domestic buildings constructed prior to 31<sup>st</sup> December 2003 must have a compliant <strong>Asbestos Register</strong> and <strong>Asbestos Management Plan</strong>.</p>
      <p>This covers all buildings in which people work – commercial, retail, industrial, community, educational, healthcare, accommodation and some strata developments.</p>
      <p>Fines of up to $30,000 apply for non-compliance.</p>
    </section>

    <section class="panel panel--right">
      <h2>What is an Asbestos Register and Management Plan?</h2>
      <p class="list-intro">An <strong>Asbestos Register</strong> must</p>
      <ul class="checklist">
        <li>Record any asbestos that has been identified or is assumed to be present at the workplace</li>
        <li>record the date when the asbestos was identified</li>
        <li>record the location, type and condition of the asbestos</li>
        <li>be maintained to ensure up-to-date information</li>
        <li>state if no asbestos has been identified</li>
        <li>be given to the person conducting a business or undertaking (PCBU) when there is a change of management or controller of the workplace.</li>
      </ul>
      <p class="list-intro">The <strong>Asbestos Management Plan</strong> must</p>
      <ul class="checklist">
        <li>identify the location of asbestos and any naturally occurring asbestos</li>
        <li>include decisions, and reasons for decisions, about the management of asbestos at the workplace for example safe work procedures and control measures</li>
        <li>outline procedures for incidents and emergencies involving asbestos, including who is responsible</li>
        <li>be maintained with up-to-date information</li>
        <li>be reviewed at least every five years or when requested by a health and safety representative (HSR) or when asbestos is removed, disturbed, sealed or enclosed, or when changes to a control measure are made or when the plan is no longer adequate.</li>
      </ul>
    </section>
  </div>
</body>
</html>
```